Ovaro Letterhead

Need a fresh looking design. We are a IT service company and I would like some elements of the logo to flow through. I have included the logo as an attachment. I have also included business card design as it might help with the design.

Industry/Entity Type

Business

```html
<!DOCTYPE html>
<html lang="en">
<head>
<meta charset="utf-8">
<title>Ovaro Letterhead</title>
<link rel="stylesheet" href="https://fonts.googleapis.com/css2?family=Open+Sans:wght@400;600;700&display=swap">
<style>
  :root {
    --backdrop: #46474c;
    --paper: #ffffff;
    --brand-green: #9dcc3f;
    --brand-grey: #6d6e72;
    --watermark: #ececed;
    --ink: #2b2b2d;
  }
  * { box-sizing: border-box; margin: 0; padding: 0; }
  html, body {
    width: 1200px;
    height: 849px;
    overflow: hidden;
    background: var(--backdrop);
    font-family: "Open Sans", Arial, sans-serif;
  }
  .letterhead {
    position: absolute;
    left: 320px;
    top: 28px;
    width: 560px;
    height: 792px;
    background: var(--paper);
    overflow: hidden;
  }
  .brand {
    position: absolute;
    left: 44px;
    top: 40px;
    display: flex;
    flex-direction: column;
    gap: 2px;
  }
  .brand-row {
    display: flex;
    align-items: center;
    gap: 8px;
  }
  .brand-square {
    width: 16px;
    height: 16px;
    background: var(--brand-green);
  }
  .brand-name {
    font-size: 32px;
    font-weight: 700;
    line-height: 1;
    color: var(--brand-green);
    letter-spacing: 0.5px;
  }
  .brand-web {
    font-size: 9px;
    font-weight: 600;
    color: var(--brand-green);
    letter-spacing: 0.6px;
  }
  .watermark-name {
    position: absolute;
    left: 0;
    right: 0;
    top: 300px;
    text-align: center;
    font-size: 150px;
    font-weight: 700;
    color: var(--watermark);
    line-height: 1;
    user-select: none;
  }
  .contact-band {
    position: absolute;
    left: 0;
    right: 0;
    bottom: 0;
    height: 30px;
    background: var(--brand-green);
    display: flex;
    align-items: center;
    justify-content: center;
    gap: 16px;
    font-size: 9px;
    color: var(--ink);
  }
  .contact-item {
    display: flex;
    align-items: center;
    gap: 5px;
  }
  .contact-icon {
    width: 10px;
    height: 10px;
    flex: none;
  }
</style>
</head>
<body>
  <main class="letterhead">
    <header class="brand">
      <div class="brand-row">
        <span class="brand-name">Ovaro</span>
        <span class="brand-square"></span>
      </div>
      <span class="brand-web">www.ovaro.com.au</span>
    </header>

    <div class="watermark-name" aria-hidden="true">Ovaro</div>

    <footer class="contact-band">
      <span class="contact-item">
        <svg class="contact-icon" viewBox="0 0 10 10"><path d="M5 1a3 3 0 0 0-3 3c0 2.2 3 5 3 5s3-2.8 3-5a3 3 0 0 0-3-3zm0 4.2a1.2 1.2 0 1 1 0-2.4 1.2 1.2 0 0 1 0 2.4z" fill="#2b2b2d"/></svg>
        PO Box 2210, Marlow 3011
      </span>
      <span class="contact-item">
        <svg class="contact-icon" viewBox="0 0 10 10"><path d="M2.3 1.2l1.4 1.6-.7 1.1c.5 1 1.2 1.7 2.2 2.2l1.1-.7 1.6 1.4-.8 1.5C4.6 8.2 1.8 5.4 1 1.9z" fill="#2b2b2d"/></svg>
        02 5550 1842
      </span>
      <span class="contact-item">
        <svg class="contact-icon" viewBox="0 0 10 10"><rect x="1.5" y="2" width="7" height="6" rx="1" fill="none" stroke="#2b2b2d" stroke-width="1"/><rect x="3" y="3.5" width="4" height="2" fill="#2b2b2d"/></svg>
        02 5550 2976
      </span>
      <span class="contact-item">
        <svg class="contact-icon" viewBox="0 0 10 10"><rect x="3" y="1" width="4" height="8" rx="0.8" fill="none" stroke="#2b2b2d" stroke-width="1"/><circle cx="5" cy="7.5" r="0.5" fill="#2b2b2d"/></svg>
        0400 555 318
      </span>
      <span class="contact-item">
        <svg class="contact-icon" viewBox="0 0 10 10"><rect x="1" y="2.5" width="8" height="5" fill="none" stroke="#2b2b2d" stroke-width="1"/><path d="M1 2.5l4 3 4-3" fill="none" stroke="#2b2b2d" stroke-width="1"/></svg>
        hi@ovaro.com.au
      </span>
    </footer>
  </main>
</body>
</html>
```